IT-support company web-site design

We need to re-design out site for existing clients and for the future promotions. Site needs to be attractive with intuitive interface. We need to keep our logo and colors but any reshuffles can be made. I provide the working site and re-made version, which we do nt like. It has to be more bright and clear. All the blocks have to be divided and look like logic and structured. PLease find the addresses to work with below.
The "real" one https://plorim.com
The version http://dostuly.net/Plorim/
If you have any с

Industry/Entity Type

It Company

Number of Pages Required

5+ page

Font styles to use
Sans Serif

Colors
9bcb3c

Requirements
Must have
• Our LOGO and our colors (green palette). We d like to make our services blocks as the main things. We need to have our images and slogans as there are extremely important advantages of our company.
Nice to have
• Original and modern view of the site.
Should not have
• unpredictable and @surprising@, hard- definable buttons and ways

```html
<!DOCTYPE html>
<html lang="en">
<head>
<meta charset="utf-8">
<title>Plorim – IT Support</title>
<link rel="stylesheet" href="https://fonts.googleapis.com/css2?family=Alegreya:wght@400&family=Montserrat:wght@400;600;700&family=Open+Sans:ital,wght@0,400;0,600;0,700;1,400;1,600&family=Righteous&display=swap">
<style>
:root{
  --green:#9bcb3c;
  --green-deep:#8cc43a;
  --green-text:#5e7f1f;
  --dark:#2c3034;
  --light:#ebebeb;
  --lighter:#f3f3f3;
  --footer:#474747;
  --footer-bottom:#3a3a3a;
  --ink:#444;
  --white:#fff;
}
*{margin:0;padding:0;box-sizing:border-box}
html,body{width:1200px;height:2250px;overflow:hidden}
body{position:relative;font-family:Arial,Helvetica,sans-serif;color:var(--ink);background:var(--white)}
.abs{position:absolute}
section,header,footer{position:absolute;left:0;width:1200px}

/* hero */
.hero{top:0;height:543px;background:linear-gradient(180deg,#3a3f45 0%,#4b5157 40%,#30353a 75%,#3e3a34 100%)}
.hero-scene{position:absolute;inset:0;background:linear-gradient(180deg,rgba(90,96,102,.5) 0%,rgba(40,44,48,.2) 50%,rgba(25,28,30,.6) 100%)}
.logo{font-family:Montserrat,sans-serif;font-weight:400;font-size:32px;letter-spacing:2px;color:var(--white);display:flex;align-items:center;gap:10px}
.logo i{display:inline-block;width:22px;height:22px;border-radius:50%;border:3px solid var(--green)}
.main-nav{top:27px;left:0;width:1200px;height:20px;font-family:Montserrat,sans-serif;font-weight:600;font-size:14px;color:var(--white)}
.main-nav span{position:absolute;white-space:nowrap}
.nav-active{position:absolute;top:0;left:390px;width:138px;height:5px;background:var(--green)}
.login{top:21px;left:985px;width:70px;height:30px;background:var(--green);color:var(--white);font-family:Montserrat,sans-serif;font-weight:600;font-size:14px;display:flex;align-items:center;justify-content:center}
.hero-kicker{top:135px;width:1200px;text-align:center;font-family:Alegreya,serif;font-size:25px;color:var(--white)}
.hero-title{top:168px;width:1200px;text-align:center;font-family:Righteous,sans-serif;font-size:48px;color:var(--green);letter-spacing:1px}
.hero-text{top:240px;left:280px;width:640px;text-align:center;font-family:Montserrat,sans-serif;font-weight:600;font-size:16px;line-height:23px;color:var(--white)}
.hero-arrow{top:225px}
.services-title{top:343px;width:1200px;text-align:center;font-family:Righteous,sans-serif;font-size:28px;color:var(--green)}
.services-title span{border-bottom:2px solid var(--green);padding-bottom:1px}
.service{top:410px;width:190px;text-align:center;color:var(--white);font-family:Montserrat,sans-serif;font-weight:700;font-size:13.5px;line-height:15px}
.service svg{display:block;margin:0 auto 20px}
.service-divider{top:405px;width:1px;height:110px;background:rgba(255,255,255,.35)}

/* about */
.about{top:543px;height:390px;background:var(--light)}
.section-title{width:1200px;text-align:center;font-family:Montserrat,sans-serif;font-weight:700;font-size:20px;color:#3a3a3a}
.title-rule{left:455px;width:290px;height:1px;background:#aaa}
.title-rule::after{content:"";position:absolute;left:123px;top:-2px;width:44px;height:4px;border-radius:2px;background:#777}
.welcome{top:100px;left:140px;font-family:Montserrat,sans-serif;font-weight:700;font-size:20px;color:#666}
.about-text{top:137px;left:140px;width:515px;font-size:15.5px;line-height:20px;color:#555}
.about-text p{text-indent:54px;margin-bottom:12px}
.btn{background:var(--green);color:var(--white);font-family:Montserrat,sans-serif;font-weight:600;font-size:16px;display:flex;align-items:center;justify-content:center}
.read-more{top:302px;left:138px;width:152px;height:45px}
.about-photo{top:85px;left:688px;width:374px;height:248px;background:var(--green);padding:9px}
.about-photo div{width:100%;height:100%;background:linear-gradient(135deg,#e9e3dc 0%,#b9b0a8 40%,#3b3a3d 75%,#f1eef0 100%)}

/* benefits */
.benefits{top:933px;height:525px;background:var(--green-deep)}
.benefits-scene{position:absolute;inset:0;background:linear-gradient(180deg,rgba(155,203,60,0) 0%,rgba(120,170,40,.35) 60%,rgba(140,190,55,.2) 100%)}
.benefits .section-title{color:var(--green-text);top:25px}
.benefits .title-rule{background:rgba(255,255,255,.7)}
.benefits .title-rule::after{background:#4f6d1a}
.benefits-text{top:83px;left:180px;width:840px;text-align:center;font-size:16px;line-height:20px;color:var(--white)}
.benefit{width:300px;text-align:center;font-family:Montserrat,sans-serif;font-weight:700;font-size:18px;line-height:21px;color:var(--white)}
.benefit svg{display:block;margin:0 auto 16px}
.benefit.muted{color:#4e6b19}

/* testimonials */
.testimonials{top:1458px;height:270px;background:var(--light)}
.block-title{left:144px;font-family:Montserrat,sans-serif;font-weight:700;font-size:18px;color:#333}
.pager{top:30px;left:1012px}
.avatar{width:108px;height:108px;border-radius:50%}
.t-name{font-family:"Open Sans",sans-serif;font-style:italic;font-weight:600;font-size:20px;color:#333}
.t-quote{width:300px;font-family:"Open Sans",sans-serif;font-style:italic;font-size:14px;line-height:18px;color:#777}
.t-by{font-family:"Open Sans",sans-serif;font-style:italic;font-size:16px;color:#333}

/* clients */
.clients{top:1728px;height:192px;background:var(--lighter)}
.client{top:105px;height:30px;display:flex;align-items:center;justify-content:center;gap:8px;font-family:Montserrat,sans-serif;font-weight:700;font-size:22px;color:#2c6a9e;white-space:nowrap}
.client i{display:inline-block;width:14px;height:14px;background:currentColor;flex:none}

/* newsletter */
.newsletter{top:1920px;height:72px;background:var(--green)}
.news-label{top:20px;left:217px;font-family:"Open Sans",sans-serif;font-size:22px;color:var(--white);letter-spacing:.5px}
.news-input{top:13px;left:502px;width:315px;height:44px;background:#efefef;font-family:"Open Sans",sans-serif;font-size:14px;color:#aaa;padding:13px 20px}
.news-btn{top:13px;left:817px;width:144px;height:44px;background:#444;color:var(--white);font-family:"Open Sans",sans-serif;font-weight:600;font-size:17px;display:flex;align-items:center;justify-content:center}

/* footer */
.site-footer{top:1992px;height:201px;background:var(--footer)}
.f-col{top:14px;font-family:"Open Sans",sans-serif;font-size:16.5px;line-height:24px;color:#e4e4e4}
.f-col h4{font-weight:700;font-size:17px;color:var(--white)}
.bottom-bar{top:2193px;height:57px;background:var(--footer-bottom)}
.social{top:18px;width:22px;height:22px}
</style>
</head>
<body>

<header class="hero">
  <div class="hero-scene" role="img" aria-label="Stormy city skyline photograph under dark clouds"></div>
  <div class="nav-active"></div>
  <div class="abs logo" style="top:16px;left:142px"><i></i>PLORIM</div>
  <nav class="abs main-nav">
    <span style="left:393px">Plorim difference</span>
    <span style="left:540px">Services</span>
    <span style="left:624px">Customers</span>
    <span style="left:718px">Resources</span>
    <span style="left:817px">Support</span>
    <span style="left:892px">About us</span>
  </nav>
  <div class="abs login">Login</div>

  <div class="abs hero-kicker">We Make Your Information Technology</div>
  <div class="abs hero-title">SECURE and SIMPLE</div>
  <p class="abs hero-text">Plorim's secure IT systems delivered 100% uninterrupted service during all hurricanes and tropical storms since 2000 including<br>Allison, Rita, Ike and Harvey.</p>
  <svg class="abs hero-arrow" style="left:100px" width="22" height="64" viewBox="0 0 22 64"><polyline points="20,2 2,32 20,62" fill="none" stroke="rgba(255,255,255,.7)" stroke-width="2"/></svg>
  <svg class="abs hero-arrow" style="left:1077px" width="22" height="64" viewBox="0 0 22 64"><polyline points="2,2 20,32 2,62" fill="none" stroke="rgba(255,255,255,.7)" stroke-width="2"/></svg>

  <div class="abs services-title"><span>OUR SERVICES</span></div>

  <div class="abs service" style="left:130px">
    <svg width="44" height="44" viewBox="0 0 44 44"><circle cx="24" cy="20" r="11" fill="none" stroke="#fff" stroke-width="3"/><line x1="32" y1="28" x2="40" y2="36" stroke="#fff" stroke-width="4"/><polyline points="19,20 23,24 29,16" fill="none" stroke="#fff" stroke-width="3"/><rect x="3" y="10" width="6" height="3" fill="#fff"/><rect x="3" y="18" width="6" height="3" fill="#fff"/><rect x="3" y="26" width="6" height="3" fill="#fff"/></svg>
    UPFRONT AUDIT
  </div>
  <div class="abs service-divider" style="left:322px"></div>
  <div class="abs service" style="left:311px">
    <svg width="60" height="44" viewBox="0 0 60 44"><circle cx="42" cy="14" r="10" fill="none" stroke="#fff" stroke-width="5" stroke-dasharray="4 3"/><circle cx="42" cy="14" r="4" fill="#fff"/><path d="M2 28h12l10 4h14l-2 5H22v2h16l14-8 4 3-16 11H2z" fill="#fff"/></svg>
    SERVICE TYPES
  </div>
  <div class="abs service-divider" style="left:502px"></div>
  <div class="abs service" style="left:503px">
    <svg width="50" height="44" viewBox="0 0 50 44"><rect x="4" y="6" width="28" height="26" rx="2" fill="#fff"/><path d="M32 14h9l6 8v10H32z" fill="#fff"/><circle cx="13" cy="35" r="5" fill="#fff" stroke="#333" stroke-width="2"/><circle cx="39" cy="35" r="5" fill="#fff" stroke="#333" stroke-width="2"/><rect x="10" y="12" width="16" height="12" fill="#555"/></svg>
    MOVING TO<br>PLORIM SYSTEM
  </div>
  <div class="abs service-divider" style="left:693px"></div>
  <div class="abs service" style="left:694px">
    <svg width="54" height="44" viewBox="0 0 54 44"><circle cx="30" cy="9" r="7" fill="#fff"/><rect x="28" y="14" width="4" height="16" fill="#fff"/><path d="M30 24c-6-6-12-4-14-2 6 2 10 4 14 2zM30 20c6-6 12-4 14-2-6 2-10 4-14 2z" fill="#fff"/><path d="M4 34h14l8 3h16l6-4 4 3-8 8H4z" fill="#fff"/></svg>
    COST SAVINGS
  </div>
  <div class="abs service-divider" style="left:888px"></div>
  <div class="abs service" style="left:892px">
    <svg width="44" height="44" viewBox="0 0 44 44"><rect x="4" y="32" width="5" height="10" fill="#fff"/><rect x="12" y="26" width="5" height="16" fill="#fff"/><rect x="20" y="20" width="5" height="22" fill="#fff"/><rect x="28" y="14" width="5" height="28" fill="#fff"/><polyline points="4,24 16,14 24,16 38,4" fill="none" stroke="#fff" stroke-width="3"/><polygon points="32,2 40,2 40,10" fill="#fff"/></svg>
    PERFORMANCE<br>TRACKING
  </div>
</header>

<section class="about">
  <div class="abs section-title" style="top:24px">ABOUT US</div>
  <div class="abs title-rule" style="top:57px"></div>
  <div class="abs welcome">Welcome To PLORIM</div>
  <div class="abs about-text">
    <p>Lorem ipsum dolor sit amet, consectetur adipiscing elit, sed do eiusmod tempor incididunt ut labore et dolore magna aliqua. Ut enim ad minim veniam.Lorem ipsum dolor sit amet, consectetur adipiscing elit, sed do eiusmod tempor incididunt ut labore et dolore magna aliqua. Ut enim ad minim veniam.</p>
    <p>sed do eiusmod tempor incididunt ut labore et dolore magna aliqua. Ut enim ad minim veniam.</p>
  </div>
  <div class="abs btn read-more">Read More</div>
  <div class="abs about-photo"><div role="img" aria-label="Photo of two business colleagues reviewing a laptop together"></div></div>
</section>

<section class="benefits">
  <div class="benefits-scene" role="img" aria-label="Faint city skyline photo behind a green overlay"></div>
  <div class="abs section-title">BENEFITS YOU CAN EXPECT WITH PLORIM</div>
  <div class="abs title-rule" style="top:62px"></div>
  <p class="abs benefits-text">Lorem ipsum dolor sit amet, consectetur adipiscing elit, sed do eiusmod tempor incididunt ut labore et dolore magna aliqua. Ut enim ad minim veniam.Lorem ipsum dolor sit amet, consectetur adipiscing elit, sed do eiusmod tempor incididunt ut labore et</p>

  <div class="abs benefit" style="top:192px;left:136px">
    <svg width="50" height="56" viewBox="0 0 50 56"><path d="M25 2 46 10v16c0 14-10 24-21 28C14 50 4 40 4 26V10z" fill="#fff"/><polyline points="14,28 22,36 36,20" fill="none" stroke="#8cc43a" stroke-width="5"/></svg>
    99.999% UPTIME<br>GUARANTEED
  </div>
  <div class="abs benefit" style="top:192px;left:434px">
    <svg width="50" height="56" viewBox="0 0 50 56"><path d="M25 2 46 10v16c0 14-10 24-21 28C14 50 4 40 4 26V10z" fill="none" stroke="#fff" stroke-width="3"/><path d="M25 9 40 15v11c0 10-7 18-15 21z" fill="#fff"/><line x1="14" y1="36" x2="34" y2="16" stroke="#8cc43a" stroke-width="3"/></svg>
    PROACTIVE SYSTEM<br>SECURITY
  </div>
  <div class="abs benefit" style="top:182px;left:732px">
    <svg width="66" height="66" viewBox="0 0 66 66"><rect x="6" y="26" width="34" height="24" fill="none" stroke="#fff" stroke-width="3"/><rect x="16" y="50" width="14" height="4" fill="#fff"/><rect x="10" y="54" width="26" height="4" fill="#fff"/><path d="M30 22l14-14 14 14z" fill="#fff" transform="rotate(45 44 18)"/><path d="M46 4a16 16 0 0 1 16 16M46 10a10 10 0 0 1 10 10" fill="none" stroke="#fff" stroke-width="3"/></svg>
    REMOTE ACCESS FROM<br>ANYWHERE IN THE WORLD
  </div>

  <div class="abs benefit muted" style="top:366px;left:136px">
    <svg width="54" height="58" viewBox="0 0 54 58"><circle cx="27" cy="20" r="13" fill="#4e6b19"/><path d="M4 56c2-16 12-20 23-20s21 4 23 20z" fill="#4e6b19"/><path d="M12 20a15 15 0 0 1 30 0" fill="none" stroke="#4e6b19" stroke-width="3"/></svg>
    PERSONALIZED<br>LOCAL 24/7/365 SUPPORT
  </div>
  <div class="abs benefit" style="top:362px;left:434px">
    <svg width="50" height="64" viewBox="0 0 50 64"><path d="M14 24V16a11 11 0 0 1 22 0v8" fill="none" stroke="#fff" stroke-width="5"/><rect x="6" y="24" width="38" height="36" rx="6" fill="#fff"/><text x="25" y="52" text-anchor="middle" font-family="Montserrat,sans-serif" font-weight="700" font-size="24" fill="#8cc43a">$</text></svg>
    PREDICTABLE COSTS
  </div>
  <div class="abs benefit" style="top:362px;left:732px">
    <svg width="70" height="64" viewBox="0 0 70 64"><rect x="16" y="20" width="30" height="22" fill="none" stroke="#fff" stroke-width="4"/><path d="M8 34a26 26 0 0 1 44-22" fill="none" stroke="#fff" stroke-width="5"/><polygon points="52,2 62,16 46,18" fill="#fff"/><path d="M62 30a26 26 0 0 1-44 22" fill="none" stroke="#fff" stroke-width="5"/><polygon points="18,62 8,48 24,46" fill="#fff"/></svg>
    BUSINESS<br>CONTINUITY AND DR
  </div>
</section>

<section class="testimonials">
  <div class="abs block-title" style="top:28px">TESTIMONIALS</div>
  <svg class="abs pager" width="60" height="20" viewBox="0 0 60 20"><polyline points="10,2 3,10 10,18" fill="none" stroke="#444" stroke-width="2"/><polyline points="40,2 47,10 40,18" fill="none" stroke="#444" stroke-width="2"/></svg>

  <div class="abs avatar" style="top:85px;left:138px;background:radial-gradient(circle at 50% 45%,#c9a58c 0%,#7a5a48 55%,#2d2b2c 100%)" role="img" aria-label="Portrait photo of a client"></div>
  <div class="abs t-name" style="top:80px;left:279px">Martin Caldwell</div>
  <p class="abs t-quote" style="top:115px;left:274px">"We didn't have the expertise or resources to keep our network up- to- date with ever-growing record keeping and patient privacy regulations. With NetSteady®, I can focus on running my practice."</p>
  <div class="abs t-by" style="top:212px;left:274px">-Martin R. Caldwell MD,PA</div>

  <div class="abs avatar" style="top:85px;left:618px;background:radial-gradient(circle at 50% 45%,#d9b9a2 0%,#8c6c5a 45%,#f4f4f4 75%)" role="img" aria-label="Portrait photo of a client"></div>
  <div class="abs t-name" style="top:80px;left:759px">Martin Caldwell</div>
  <p class="abs t-quote" style="top:115px;left:754px">"We didn't have the expertise or resources to keep our network up- to- date with ever-growing record keeping and patient privacy regulations. With NetSteady®, I can focus on running my practice."</p>
  <div class="abs t-by" style="top:212px;left:754px">-Martin R. Caldwell MD,PA</div>
</section>

<section class="clients">
  <div class="abs block-title" style="top:27px">WHO'S USING NETSTEADY®?</div>
  <svg class="abs pager" width="60" height="20" viewBox="0 0 60 20"><polyline points="10,2 3,10 10,18" fill="none" stroke="#444" stroke-width="2"/><polyline points="40,2 47,10 40,18" fill="none" stroke="#444" stroke-width="2"/></svg>
  <div class="abs client" style="left:156px;width:180px;color:#1f5fa6"><i></i>BRAVANE</div>
  <div class="abs client" style="left:354px;width:200px;color:#2d3a1a">TELMOR</div>
  <div class="abs client" style="left:570px;width:240px;color:#1a5d7a"><i></i>HARLOW CRANE</div>
  <div class="abs client" style="left:815px;width:220px;color:#888;font-weight:400">Openfield</div>
</section>

<section class="newsletter">
  <div class="abs news-label">JOIN OUR NEWSLETTER :</div>
  <div class="abs news-input">Enter your e-mail address</div>
  <div class="abs news-btn">SUBSCRIBE</div>
</section>

<footer class="site-footer">
  <div class="abs f-col" style="left:157px"><h4>Plorim Difference</h4>Core Benefits<br>Side by Side Com-<br>parison<br>vs. IT Consultants<br>vs. In-house<br>vs. Outsourcing</div>
  <div class="abs f-col" style="left:420px"><h4>Services</h4>Upfront Audit<br>Service Types<br>Moving to Plorim System<br>Cost Savings<br>Performance Tracking</div>
  <div class="abs f-col" style="left:686px"><h4>Resources</h4>FAQ's<br>Helpful Tips<br>White Papers<br>Brochures<br>Booklets</div>
  <div class="abs f-col" style="left:885px"><h4>Customers</h4>Who do we help<br>Roles<br>Testimonials<br>Case Studies<br>Customer Logos</div>
</footer>

<footer class="bottom-bar">
  <div class="abs logo" style="top:10px;left:145px"><i></i>PLORIM</div>
  <div class="abs social" style="left:935px;background:#3b8fd6"></div>
  <div class="abs social" style="left:966px;background:#3b5a9a"></div>
  <div class="abs social" style="left:998px;background:#d84a38"></div>
  <div class="abs social" style="left:1031px;background:#d42b2b"></div>
</footer>

</body>
</html>
```